Wedding Invitations

We are a printing company "inkmorrow" and require multiple wedding invitation designs for our customers in store and online. We would like the designs to be editable in Photoshop if possible, if not then a layout with suggested fonts would be the next best option. We are open to suggestions on design but would like to stick to the general wedding themes some with a modern and some with a classical feel

Industry/Entity Type

Printing

```html
<!DOCTYPE html>
<html lang="en">
<head>
<meta charset="utf-8">
<title>Wedding Invitation Set – inkmorrow</title>
<link href="https://fonts.googleapis.com/css2?family=Poiret+One&family=Delius&family=Lobster&family=Dancing+Script:wght@600&display=swap" rel="stylesheet">
<style>
  :root{
    --stage:#99ad6f;
    --wine:#5c1e31;
    --wine-soft:#6e2c3d;
    --gold:#ffcf1a;
    --amber:#e8952e;
    --rust:#c8683a;
    --label:#222;
  }
  *{box-sizing:border-box;margin:0;padding:0}
  html,body{width:1200px;height:928px;overflow:hidden}
  body{background:var(--stage);position:relative;font-family:"Delius",sans-serif;color:var(--gold)}
  .view-label{position:absolute;top:26px;font:16px Arial,sans-serif;color:var(--label);letter-spacing:.5px;transform:translateX(-50%)}
  .card{position:absolute;background:var(--wine);overflow:hidden;box-shadow:0 1px 4px rgba(0,0,0,.35)}
  .ornament{position:absolute;background:var(--wine-soft);opacity:.45;border-radius:40%}

  /* inside */
  .inside{left:189px;top:57px;width:359px;height:492px}
  .inside .families{position:absolute;top:72px;width:100%;text-align:center;font-size:8px}
  .names{position:absolute;top:98px;left:0;width:100%;font-family:"Poiret One",sans-serif;font-size:29px;line-height:31px;font-weight:700}
  .names .groom{position:absolute;left:40px;width:130px;text-align:center}
  .names .bride{position:absolute;left:218px;width:134px;text-align:center}
  .names .amp{position:absolute;left:182px;top:14px;font-family:"Delius",sans-serif;font-size:30px}
  .details{position:absolute;top:282px;width:100%;text-align:center;font-size:10.5px;line-height:13.5px}
  .details p+p{margin-top:6px}
  .reception{position:absolute;top:432px;width:100%;text-align:center;font-family:"Dancing Script",cursive;font-size:17px}

  /* outside */
  .outside{left:611px;top:57px;width:402px;height:492px}
  .panel{position:absolute;left:0;width:402px;height:247px;overflow:hidden}
  .panel-verse{top:0;height:245px}
  .panel-front{top:245px;background:var(--wine)}
  .bloom{position:absolute;inset:0;background:linear-gradient(180deg,#e89b2c 0%,#d27a2c 45%,#9a3d2d 80%,var(--wine) 100%)}
  .verse-flip{position:absolute;inset:0;transform:rotate(180deg)}
  .verse-title{position:absolute;font-family:"Dancing Script",cursive;font-size:34px;color:var(--gold)}
  .verse-text{position:absolute;font-size:9.5px;line-height:11px;text-align:center;color:var(--gold)}

  .front-curve{position:absolute;inset:0}
  .front-title{position:absolute;left:30px;top:22px;font-family:"Lobster",cursive;font-size:28px}
  .front-date{position:absolute;left:42px;top:58px;font-size:8px}
  .front-groom{position:absolute;left:88px;top:92px;font-family:"Dancing Script",cursive;font-size:32px}
  .front-amp{position:absolute;left:130px;top:132px;font-family:"Dancing Script",cursive;font-size:12px}
  .front-bride{position:absolute;left:128px;top:140px;font-family:"Dancing Script",cursive;font-size:32px}
  .stamp-box{position:absolute;left:271px;top:179px;width:82px;height:44px;border:1.5px solid var(--gold);border-radius:4px}

  /* loose cards */
  .verse-card{left:236px;top:600px;width:334px;height:250px;transform:rotate(-10deg);background:linear-gradient(20deg,#e98f2a 0%,#d7772d 40%,#8c3a2e 62%,var(--wine) 75%)}
  .front-card{left:510px;top:644px;width:403px;height:248px}
</style>
</head>
<body>

<span class="view-label" style="left:382px">INSIDE</span>
<span class="view-label" style="left:817px">OUTSIDE</span>

<!-- inside of invitation -->
<section class="card inside">
  <div class="ornament" role="img" aria-label="faint swirl flourish" style="left:-10px;top:10px;width:90px;height:230px"></div>
  <div class="ornament" role="img" aria-label="faint swirl flourish" style="left:270px;top:10px;width:95px;height:230px"></div>
  <div class="ornament" role="img" aria-label="faint butterfly silhouettes" style="left:245px;top:345px;width:105px;height:110px"></div>

  <p class="families">Together with their families</p>
  <div class="names">
    <div class="groom">DANIEL<br>ELLIOT</div>
    <div class="amp">&amp;</div>
    <div class="bride">CLARA<br>WESTON</div>
  </div>
  <div class="details">
    <p>Mr. and Mrs. Howard Bennett Lorimer<br>Request the honour of your presence<br>at the marriage of their daughter</p>
    <p>Wednesday, the ninth of June two thousand and fourteen<br>at six o'clock in the evening</p>
    <p>Hollins Ridge Country Club<br>218 Willow Bend Lane<br>Ashford, North Carolina</p>
  </div>
  <p class="reception">Reception to follow</p>
</section>

<!-- outside of invitation, folded flat -->
<section class="card outside">
  <div class="panel panel-verse">
    <div class="bloom" role="img" aria-label="orange lily flowers photograph"></div>
    <div class="verse-flip">
      <div class="verse-title" style="left:140px;top:58px">Marriage</div>
      <p class="verse-text" style="left:60px;top:112px;width:280px">Marriage is caring and sharing,<br>giving and forgiving,<br>loving and being loved, walking hand in hand,<br>talking heart to heart, to give and to take<br>and to see through each others eyes.</p>
    </div>
  </div>
  <div class="panel panel-front">
    <svg class="front-curve" width="402" height="247" viewBox="0 0 402 247" aria-hidden="true">
      <defs><linearGradient id="curveFill" x1="0" y1="0" x2="1" y2="0"><stop offset="0" stop-color="#b8583b"/><stop offset="1" stop-color="#d9793c"/></linearGradient></defs>
      <path d="M290 0 C345 70 320 185 150 247 L402 247 L402 0 Z" fill="url(#curveFill)"/>
    </svg>
    <div class="ornament" role="img" aria-label="faint swirl flourish" style="left:20px;top:110px;width:70px;height:130px"></div>
    <div class="ornament" role="img" aria-label="faint floral flourish" style="left:300px;top:6px;width:90px;height:90px;background:#d48a68"></div>
    <div class="front-title">The Wedding</div>
    <div class="front-date">Wednesday, June 9th 2014</div>
    <div class="front-groom">Elliot</div>
    <div class="front-amp">&amp;</div>
    <div class="front-bride">Clara</div>
    <div class="stamp-box"></div>
  </div>
</section>

<!-- loose verse card -->
<section class="card verse-card">
  <div class="bloom" role="img" aria-label="orange lily flowers photograph" style="background:transparent"></div>
  <div class="verse-title" style="left:112px;top:28px">Marriage</div>
  <p class="verse-text" style="left:60px;top:84px;width:250px">Marriage is caring and sharing,<br>giving and forgiving,<br>loving and being loved, walking hand in hand,<br>talking heart to heart, to give and to take<br>and to see through each others eyes.</p>
</section>

<!-- loose front card -->
<section class="card front-card">
  <svg class="front-curve" width="403" height="248" viewBox="0 0 402 247" aria-hidden="true">
    <path d="M290 0 C345 70 320 185 150 247 L402 247 L402 0 Z" fill="url(#curveFill)"/>
  </svg>
  <div class="ornament" role="img" aria-label="faint swirl flourish" style="left:20px;top:110px;width:70px;height:130px"></div>
  <div class="ornament" role="img" aria-label="faint floral flourish" style="left:300px;top:6px;width:90px;height:90px;background:#d48a68"></div>
  <div class="front-title">The Wedding</div>
  <div class="front-date">Wednesday, June 9th 2014</div>
  <div class="front-groom">Elliot</div>
  <div class="front-amp">&amp;</div>
  <div class="front-bride">Clara</div>
  <div class="stamp-box"></div>
</section>

</body>
</html>
```